Flyer für Mobile Massage am Arbeitsplatz
Zielgruppe
Der Flyer richtet sich an Geschäftsleitungen, Firmenvorstände, Betriebsräte.
Ich werde den Flyer sowohl persönlich überreichen, als auch postalisch verschicken.
Aufgabenstellung
Es geht um einen Flyer, DIN lang, Hochformat, beidseitig bedruckt.

```html
<!DOCTYPE html>
<html lang="de">
<head>
<meta charset="utf-8">
<title>Mobile Massage am Arbeitsplatz – Flyer</title>
<link href="https://fonts.googleapis.com/css2?family=Tinos:ital,wght@0,400;0,700;1,400;1,700&display=swap" rel="stylesheet">
<style>
  :root {
    --canvas: #ffffff;
    --paper-light: #f6f1e6;
    --paper-dark: #e9dfcc;
    --ink-brown: #5b2f14;
    --ink-text: #3a1f0e;
    --band-top: #7a4a1c;
    --band-mid: #a0692c;
    --band-dark: #5e3512;
    --photo-warm: #b58a55;
    --photo-deep: #6e4a28;
    --photo-gold: #d2a64a;
  }
  * { box-sizing: border-box; margin: 0; padding: 0; }
  html, body { width: 1200px; height: 900px; overflow: hidden; background: var(--canvas); }
  body { position: relative; font-family: "Tinos", "Times New Roman", serif; }

  .flyer-page {
    position: absolute;
    top: 60px;
    width: 544px;
    height: 762px;
    background: radial-gradient(ellipse at 50% 35%, var(--paper-light) 0%, var(--paper-dark) 100%);
    box-shadow: 0 2px 8px rgba(0,0,0,0.25);
    overflow: hidden;
  }
  .flyer-page--front { left: 57px; }
  .flyer-page--back { left: 630px; }

  .front-title {
    position: absolute;
    top: 140px;
    width: 100%;
    text-align: center;
    font-style: italic;
    font-size: 50px;
    line-height: 66px;
    color: var(--ink-brown);
    text-shadow: 2px 2px 3px rgba(90,50,20,0.45);
  }
  .front-phone {
    position: absolute;
    top: 418px;
    width: 100%;
    text-align: center;
    font-style: italic;
    font-size: 30px;
    color: var(--ink-brown);
    text-shadow: 1px 1px 2px rgba(90,50,20,0.35);
  }

  .photo-strip {
    position: absolute;
    top: 518px;
    left: 0;
    width: 100%;
    height: 169px;
    display: flex;
    gap: 3px;
    background: var(--canvas);
  }
  .photo-strip__cell {
    height: 100%;
    background: linear-gradient(160deg, var(--photo-warm) 0%, var(--photo-gold) 45%, var(--photo-deep) 100%);
  }
  .photo-strip__cell--wide { flex: 0 0 195px; }
  .photo-strip__cell--narrow { flex: 0 0 123px; }
  .photo-strip__cell--rest { flex: 1; }

  .footer-band {
    position: absolute;
    top: 695px;
    left: 0;
    width: 100%;
    height: 67px;
    background: linear-gradient(180deg, var(--band-mid) 0%, var(--band-top) 40%, var(--band-dark) 100%);
    color: #ffffff;
    font-style: italic;
    font-size: 19px;
    text-align: center;
    line-height: 67px;
  }
  .footer-gap {
    position: absolute;
    top: 687px;
    left: 0;
    width: 100%;
    height: 8px;
    background: var(--canvas);
  }

  .back-backdrop {
    position: absolute;
    top: 190px;
    right: 0;
    width: 250px;
    height: 320px;
    background: radial-gradient(ellipse at 60% 50%, rgba(200,170,90,0.35) 0%, rgba(200,170,90,0.12) 55%, rgba(233,223,204,0) 80%);
  }
  .back-intro {
    position: absolute;
    top: 22px;
    left: 72px;
    width: 354px;
    font-size: 15.5px;
    line-height: 21.6px;
    color: var(--ink-text);
    text-align: justify;
    hyphens: manual;
  }
  .back-intro__initial { font-size: 26px; line-height: 18px; }
  .back-tax {
    position: absolute;
    top: 290px;
    left: 58px;
    width: 380px;
    text-align: center;
    font-weight: 700;
    font-style: italic;
    font-size: 15.5px;
    line-height: 21px;
    color: var(--ink-brown);
  }
  .back-prices {
    position: absolute;
    top: 402px;
    left: 58px;
    width: 380px;
    text-align: center;
    font-size: 15.5px;
    line-height: 21px;
    color: var(--ink-text);
  }
  .back-prices__label { font-weight: 700; font-style: italic; color: var(--ink-brown); }
</style>
</head>
<body>

<section class="flyer-page flyer-page--front">
  <h1 class="front-title">Mobile Massage<br>am<br>Arbeitsplatz</h1>
  <p class="front-phone">Tel.: 030 - 48213907</p>
  <div class="photo-strip">
    <div class="photo-strip__cell photo-strip__cell--wide" role="img" aria-label="Foto: Masseur behandelt Hände einer Frau auf dem Massagestuhl"></div>
    <div class="photo-strip__cell photo-strip__cell--narrow" role="img" aria-label="Foto: Nackenmassage in Nahaufnahme"></div>
    <div class="photo-strip__cell photo-strip__cell--rest" role="img" aria-label="Foto: Rückenmassage auf dem gelben Massagestuhl"></div>
  </div>
  <div class="footer-gap"></div>
  <footer class="footer-band">www.massage-mobil-beispiel.de</footer>
</section>

<section class="flyer-page flyer-page--back">
  <div class="back-backdrop" role="img" aria-label="Blasses Hintergrundfoto: Person auf einem Massagestuhl"></div>
  <p class="back-intro"><span class="back-intro__initial">I</span>n unseren Massagen am Arbeitsplatz lassen wir Elemente aus der Shiatsu - Energiemassage und den Joint Release - Gelenklockerungen zusam&shy;menfließen. Auf diese Weise eröffnen wir einen Raum für spürbare Entspannung mitten im Ar&shy;beitsalltag. Die Massagen befreien aus berufsbe&shy;dingten Zwangshaltungen,wirken stresslindernd und stimmungshebend im team , fokussieren auf die Problemzonen im Büro: Rücken, Nacken, Schulter und Maushand und sind ein Baustein im innerbetrieblichen Gesundheitsmanagement.</p>
  <p class="back-tax">Die Kosten können, sofern vom Arbeitgeber getra-<br>gen, nach §3 Nr.34 EstG von der Steuer abgesetzt<br>werden.</p>
  <p class="back-prices"><span class="back-prices__label">Preise:</span><br>20 Minuten : 16 Euro<br>inklusive Anfahrt<br>buchbar ab 4 Personen</p>
  <div class="photo-strip">
    <div class="photo-strip__cell photo-strip__cell--wide" role="img" aria-label="Foto: Masseur behandelt Hände einer Frau auf dem Massagestuhl"></div>
    <div class="photo-strip__cell photo-strip__cell--narrow" role="img" aria-label="Foto: Nackenmassage in Nahaufnahme"></div>
    <div class="photo-strip__cell photo-strip__cell--rest" role="img" aria-label="Foto: Rückenmassage auf dem gelben Massagestuhl"></div>
  </div>
  <div class="footer-gap"></div>
  <footer class="footer-band">www.massage-mobil-beispiel.de</footer>
</section>

</body>
</html>
```